Criação de Folder para Automotivo
A empresa queria:
" A Vortan temos o seu histórico e outros elementos mais. A destacar que a Vortan se caracteriza pela qualidade dos seus produtos, possuindo cerca de 350 produtos certificados pelo BRANQUAL. "

```html
<!DOCTYPE html>
<html lang="pt-BR">
<head>
<meta charset="utf-8">
<title>Vortan Pistões – Índice</title>
<link href="https://fonts.googleapis.com/css2?family=Exo+2:ital,wght@0,400;0,700;1,700;1,800&family=Montserrat:wght@400;500&display=swap" rel="stylesheet">
<style>
  :root{
    --backdrop:#8a8a8a;
    --paper:#ffffff;
    --red:#e3262b;
    --red-deep:#b3151a;
    --ink:#2b2b2b;
    --dark:#2a2a2c;
    --steel:#6d6e72;
  }
  *{margin:0;padding:0;box-sizing:border-box}
  html,body{width:1200px;height:1200px;overflow:hidden;background:var(--backdrop)}
  .page{position:absolute;left:173px;top:0;width:854px;height:1200px;background:var(--paper);overflow:hidden}
  .header-photo{position:absolute;left:0;top:0;width:854px;height:110px;
    background:linear-gradient(90deg,#3a3b3e 0%,#7d7e82 45%,#5a5b5f 75%,#9a9b9f 100%)}
  .header-title{position:absolute;left:38px;top:28px;font:italic 700 40px/1 "Exo 2",sans-serif;color:#fff;letter-spacing:1px}
  .deco{position:absolute;left:0;top:0}
  .side-photo{position:absolute;left:0;top:110px;width:206px;height:982px;
    background:linear-gradient(180deg,#c41b20 0%,#e0383c 35%,#9e1418 60%,#d0282c 80%,#6a0e10 100%)}
  .side-brand{position:absolute;left:103px;top:330px;transform:translate(-50%,-50%) rotate(90deg);
    display:flex;flex-direction:column;align-items:center;color:#fff;white-space:nowrap}
  .side-brand .name{font:700 54px/1 "Exo 2",sans-serif;letter-spacing:10px;text-transform:uppercase}
  .side-brand .tag{font:500 13px/1 Montserrat,sans-serif;letter-spacing:4px;margin-top:6px}
  .side-mark{position:absolute;left:86px;top:156px;width:34px;height:34px;background:#fff}
  .index{position:absolute;left:343px;top:262px;width:420px}
  .category{margin-bottom:42px}
  .category h2{font:italic 800 21px/1 "Exo 2",sans-serif;color:var(--red);letter-spacing:1px;margin-bottom:28px}
  .row{display:flex;font:400 17.5px/24px Montserrat,sans-serif;color:var(--ink)}
  .row .label{width:300px}
  .footer-photo{position:absolute;left:0;top:1092px;width:854px;height:108px;
    background:linear-gradient(90deg,#2e2f32 0%,#6a6b70 40%,#4a4b4f 70%,#8a8b90 100%)}
  .footer-brand{position:absolute;left:44px;top:1128px;font:700 38px/1 "Exo 2",sans-serif;color:#fff;letter-spacing:2px;text-transform:uppercase}
  .contacts{position:absolute;left:120px;top:1136px;width:620px;display:flex;justify-content:center;gap:14px;
    font:500 10.5px/1 Montserrat,sans-serif;color:#fff}
  .contacts span::before{content:"";display:inline-block;width:8px;height:8px;border-radius:50%;background:var(--red);margin-right:5px;vertical-align:-1px}
  .website{position:absolute;left:120px;top:1172px;width:620px;text-align:center;font:500 14px/1 Montserrat,sans-serif;color:#fff;letter-spacing:6px}
  .page-number{position:absolute;right:38px;top:1130px;font:700 34px/1 "Exo 2",sans-serif;color:var(--red)}
</style>
</head>
<body>
<div class="page">
  <div class="header-photo" role="img" aria-label="Fotografia de pistões automotivos em tons de cinza"></div>
  <h1 class="header-title">ÍNDICE</h1>
  <svg class="deco" width="854" height="1200" viewBox="0 0 854 1200">
    <polygon points="206,110 854,110 854,1092 206,1092" fill="#fff"/>
    <polygon points="672,0 762,0 652,132 562,132" fill="var(--red)"/>
    <polygon points="790,0 854,0 854,46 752,132 706,132" fill="#fff"/>
    <polygon points="830,0 854,0 854,132 724,132" fill="var(--red)" opacity="0"/>
    <polygon points="752,132 854,46 854,132" fill="var(--red)"/>
    <polygon points="655,1092 854,1092 854,1068 680,1068" fill="var(--red)"/>
  </svg>
  <div class="side-photo" role="img" aria-label="Fotografia em tom vermelho de mãos montando um motor"></div>
  <div class="side-mark"></div>
  <div class="side-brand"><span class="name">Vortan</span><span class="tag">PISTÕES</span></div>

  <section class="index">
    <div class="category">
      <h2>CATEGORIA 1</h2>
      <div class="row"><span class="label">Subcategoria 01</span><span>Pág. 01</span></div>
      <div class="row"><span class="label">Subcategoria 01</span><span>Pág. 01</span></div>
      <div class="row"><span class="label">Subcategoria 01</span><span>Pág. 01</span></div>
      <div class="row"><span class="label">Subcategoria 01</span><span>Pág. 01</span></div>
      <div class="row"><span class="label">Subcategoria 01</span><span>Pág. 01</span></div>
      <div class="row"><span class="label">Subcategoria 01</span><span>Pág. 01</span></div>
    </div>
    <div class="category">
      <h2>CATEGORIA 1</h2>
      <div class="row"><span class="label">Subcategoria 01</span><span>Pág. 01</span></div>
      <div class="row"><span class="label">Subcategoria 01</span><span>Pág. 01</span></div>
      <div class="row"><span class="label">Subcategoria 01</span><span>Pág. 01</span></div>
      <div class="row"><span class="label">Subcategoria 01</span><span>Pág. 01</span></div>
      <div class="row"><span class="label">Subcategoria 01</span><span>Pág. 01</span></div>
      <div class="row"><span class="label">Subcategoria 01</span><span>Pág. 01</span></div>
    </div>
    <div class="category">
      <h2>CATEGORIA 1</h2>
      <div class="row"><span class="label">Subcategoria 01</span><span>Pág. 01</span></div>
      <div class="row"><span class="label">Subcategoria 01</span><span>Pág. 01</span></div>
      <div class="row"><span class="label">Subcategoria 01</span><span>Pág. 01</span></div>
      <div class="row"><span class="label">Subcategoria 01</span><span>Pág. 01</span></div>
      <div class="row"><span class="label">Subcategoria 01</span><span>Pág. 01</span></div>
      <div class="row"><span class="label">Subcategoria 01</span><span>Pág. 01</span></div>
    </div>
  </section>

  <div class="footer-photo" role="img" aria-label="Fotografia de pistões enfileirados"></div>
  <div class="footer-brand">Vortan</div>
  <div class="contacts">
    <span>+55 (11) 2400-0110</span>
    <span>+55 (19) 3500-0220</span>
    <span>+55 (19) 90000-0330</span>
  </div>
  <div class="website">www.vortan.com.br</div>
  <div class="page-number">3</div>
</div>
</body>
</html>
```